Bref créative
Business Card for financial advisor
RVT Service Providers
Simple
Irina Lebedinskaya
Director
42 Marlow Yard
London
SW9 3QT
irina.lebedinskaya@rvtsupport.example

```html
<!DOCTYPE html>
<html lang="en">
<head>
<meta charset="utf-8">
<title>RVT Service Providers – Business Card</title>
<link rel="stylesheet" href="https://fonts.googleapis.com/css2?family=Open+Sans:wght@400;600;700&display=swap">
<style>
  :root {
    --backdrop: #6a6a6a;
    --card-white: #ffffff;
    --brand-red: #c8202b;
    --accent-grey: #3b3b3b;
    --ink: #3a3a3a;
    --ink-soft: #2e2e2e;
    --rule: #bdbdbd;
  }
  html, body {
    margin: 0;
    width: 1200px;
    height: 947px;
    overflow: hidden;
    background: var(--backdrop);
    font-family: "Open Sans", Arial, sans-serif;
  }
  .business-card {
    position: absolute;
    left: 133px;
    top: 230px;
    width: 903px;
    height: 520px;
    border-radius: 46px;
    background: var(--card-white);
    overflow: hidden;
  }
  .header-band {
    position: absolute;
    inset: 0;
    width: 903px;
    height: 520px;
  }
  .holder-name {
    position: absolute;
    right: 36px;
    top: 36px;
    margin: 0;
    color: var(--card-white);
    font-size: 27px;
    font-weight: 700;
    line-height: 1;
  }
  .holder-title {
    position: absolute;
    right: 36px;
    top: 73px;
    margin: 0;
    color: var(--card-white);
    font-size: 20px;
    font-weight: 700;
    line-height: 1;
  }
  .company-name {
    position: absolute;
    left: 38px;
    top: 212px;
    margin: 0;
    color: var(--ink);
    font-size: 62px;
    font-weight: 600;
    letter-spacing: -1px;
    line-height: 1;
  }
  .contact-list {
    position: absolute;
    left: 38px;
    top: 388px;
    margin: 0;
    padding: 0;
    list-style: none;
  }
  .contact-list li {
    display: flex;
    align-items: center;
    height: 33px;
    font-size: 18px;
    color: var(--ink-soft);
  }
  .contact-list svg {
    width: 18px;
    height: 18px;
    margin-right: 16px;
    fill: var(--ink-soft);
  }
  .contact-divider {
    position: absolute;
    left: 473px;
    top: 379px;
    width: 2px;
    height: 102px;
    background: var(--rule);
  }
  .postal-address {
    position: absolute;
    left: 514px;
    top: 421px;
    margin: 0;
    font-style: normal;
    font-size: 18px;
    line-height: 33px;
    color: var(--ink-soft);
  }
</style>
</head>
<body>
  <section class="business-card">
    <svg class="header-band" viewBox="0 0 903 520" aria-hidden="true">
      <path fill="var(--brand-red)" d="M0,0 H903 V250 Q480,20 0,62 Z"/>
      <path fill="none" stroke="var(--accent-grey)" stroke-width="10" d="M0,70 Q480,28 903,262"/>
    </svg>

    <h1 class="holder-name">Irina Lebedinskaya</h1>
    <p class="holder-title">Director</p>

    <p class="company-name">RVT Service Providers</p>

    <ul class="contact-list">
      <li>
        <svg viewBox="0 0 24 24" aria-hidden="true"><path d="M6.6 10.8a15.1 15.1 0 0 0 6.6 6.6l2.2-2.2a1 1 0 0 1 1-.25 11.4 11.4 0 0 0 3.6.57 1 1 0 0 1 1 1V20a1 1 0 0 1-1 1A17 17 0 0 1 3 4a1 1 0 0 1 1-1h3.5a1 1 0 0 1 1 1c0 1.25.2 2.45.57 3.57a1 1 0 0 1-.25 1z"/></svg>
        +44 (0) 207 555 0148
      </li>
      <li>
        <svg viewBox="0 0 24 24" aria-hidden="true"><path d="M7 1h10a2 2 0 0 1 2 2v18a2 2 0 0 1-2 2H7a2 2 0 0 1-2-2V3a2 2 0 0 1 2-2zm0 3v13h10V4zm5 15a1.2 1.2 0 1 0 0 2.4 1.2 1.2 0 0 0 0-2.4z"/></svg>
        irina.lebedinskaya@rvtsupport.example
      </li>
      <li>
        <svg viewBox="0 0 24 24" aria-hidden="true"><path d="M2 6a2 2 0 0 1 2-2h16a2 2 0 0 1 2 2v12a2 2 0 0 1-2 2H4a2 2 0 0 1-2-2zm2 .5V8l8 5 8-5V6.5l-8 5z"/></svg>
        irina.lebedinskaya@rvtsupport.example
      </li>
    </ul>

    <div class="contact-divider"></div>

    <address class="postal-address">
      42 Marlow Yard<br>
      London, SW9 3QT
    </address>
  </section>
</body>
</html>
```